Business card for different employees

A professional new updated design incorporating our current business's color themes and styles such as our on-site service trucks decals included in pictures attached. Our current business card is very simple and not professionally designed. We are a small family business but want a professional corporate look.

Target Market(s)

Cards to be handed out to new customers , corperate meetings. For our on site service operators.

Industry/Entity Type

Hydraulic

Contact Information for Business Card

Address, website, phone number, email, logo.
slogan - "Industry chosen hose and fittings provider".
24/7 on-site service , supply and hose management
Experienced , indpendant , family owned

Font styles to use
Sans Serif

Requirements
Must have
• Easily editable so that I can add different names and different roles for employees etc.
Nice to have
• Freedom with colour doesn't necessarily have to be blue but that is our company colour theme with trucks and logo so makes sense for the card to have blue like the trucks.

```html
<!DOCTYPE html>
<html lang="en">
<head>
<meta charset="utf-8">
<title>Meridian Hose and Fittings – Business Card</title>
<link href="https://fonts.googleapis.com/css2?family=Open+Sans:wght@400;600;700;800&family=Oswald:wght@600&display=swap" rel="stylesheet">
<style>
  :root {
    --brand-blue: #1f3fd1;
    --ink: #1d1d1f;
    --ink-soft: #4a4a4f;
    --paper: #ffffff;
    --stage: #2b2d31;
    --rule: #2a44c9;
  }
  * { box-sizing: border-box; margin: 0; padding: 0; }
  html, body { width: 1200px; height: 900px; overflow: hidden; }
  body {
    background: var(--stage);
    font-family: "Open Sans", Arial, sans-serif;
    display: flex; flex-direction: column; align-items: center; justify-content: center;
    gap: 50px;
  }
  .card {
    position: relative;
    width: 630px; height: 360px;
    background: var(--paper);
    border-radius: 22px;
    overflow: hidden;
  }
  .card-art { position: absolute; inset: 0; width: 100%; height: 100%; }

  /* brand lockup */
  .brand { position: absolute; display: flex; align-items: center; gap: 14px; }
  .brand-dot {
    width: 58px; height: 58px; border-radius: 50%;
    background: var(--ink);
    flex: none;
  }
  .brand-name {
    font-weight: 800; color: var(--brand-blue);
    font-size: 38px; line-height: 1; letter-spacing: 1px; text-transform: uppercase;
  }
  .brand-name small {
    display: block; font-size: 16px; letter-spacing: 4px; margin-top: 6px;
  }

  /* front */
  .card-front .brand { left: 150px; top: 88px; }
  .service-list {
    position: absolute; left: 70px; top: 232px;
    color: var(--paper); font-size: 19px; font-weight: 600; line-height: 1.6;
    list-style: none;
  }
  .service-list li::before { content: "• "; }

  /* back */
  .card-back .brand { left: 150px; top: 30px; }
  .brand-compact .brand-dot { width: 50px; height: 50px; }
  .brand-compact .brand-name { font-size: 34px; }
  .brand-compact .brand-name small { font-size: 14px; letter-spacing: 3px; }

  .person { position: absolute; left: 36px; top: 130px; width: 210px; text-align: right; }
  .person-name {
    font-family: "Oswald", "Arial Narrow", sans-serif; font-weight: 600;
    font-size: 30px; line-height: 1.15; color: var(--brand-blue); text-transform: uppercase; letter-spacing: .5px;
  }
  .person-role { font-size: 15px; color: var(--ink-soft); margin-top: 4px; }

  .divider {
    position: absolute; left: 262px; top: 126px; width: 2px; height: 132px;
    background: var(--rule);
  }
  .contact-list {
    position: absolute; left: 285px; top: 126px;
    list-style: none; font-size: 16px; color: var(--ink); line-height: 1.55;
  }
  .contact-list li { display: flex; align-items: flex-start; gap: 10px; }
  .contact-list svg { width: 14px; height: 14px; margin-top: 5px; flex: none; fill: var(--brand-blue); }
  .contact-list .no-icon { padding-left: 24px; }

  .slogan {
    position: absolute; right: 34px; bottom: 17px;
    color: var(--paper); font-weight: 700; font-size: 19px; line-height: 1.2;
  }
</style>
</head>
<body>

  <section class="card card-front" aria-label="Card front">
    <svg class="card-art" viewBox="0 0 630 360" preserveAspectRatio="none" aria-hidden="true">
      <polygon points="0,180 630,180 630,360 0,360" fill="var(--brand-blue)"/>
      <rect x="150" y="178" width="420" height="14" fill="var(--ink)"/>
    </svg>
    <div class="brand">
      <span class="brand-dot"></span>
      <span class="brand-name">Meridian<small>Hose and Fittings</small></span>
    </div>
    <ul class="service-list">
      <li>24/7 on-site service • Supply and hose management</li>
      <li>Experienced, indpendant, family owned</li>
    </ul>
  </section>

  <section class="card card-back" aria-label="Card back">
    <svg class="card-art" viewBox="0 0 630 360" preserveAspectRatio="none" aria-hidden="true">
      <polygon points="0,308 166,308 190,290 630,290 630,298 194,298 170,316 0,316" fill="var(--ink)"/>
      <polygon points="0,316 170,316 194,298 630,298 630,360 0,360" fill="var(--brand-blue)"/>
    </svg>

    <div class="brand brand-compact">
      <span class="brand-dot"></span>
      <span class="brand-name">Meridian<small>Hose and Fittings</small></span>
    </div>

    <div class="person">
      <p class="person-name">Daniel Carter</p>
      <p class="person-role">CEO/Managing Director</p>
    </div>

    <div class="divider"></div>

    <ul class="contact-list">
      <li><svg viewBox="0 0 24 24"><path d="M6.6 10.8a15 15 0 0 0 6.6 6.6l2.2-2.2c.3-.3.7-.4 1-.2 1.1.4 2.3.6 3.6.6.6 0 1 .4 1 1V20c0 .6-.4 1-1 1A17 17 0 0 1 3 4c0-.6.4-1 1-1h3.5c.6 0 1 .4 1 1 0 1.3.2 2.5.6 3.6.1.3 0 .7-.2 1z"/></svg>0412 555 318</li>
      <li><svg viewBox="0 0 24 24"><path d="M2 5h20v14H2zm2 2v.5l8 5 8-5V7l-8 5z"/></svg>meridianhose@mail.com</li>
      <li><svg viewBox="0 0 24 24"><path d="M12 2a10 10 0 1 0 0 20 10 10 0 0 0 0-20zm0 2c1.2 1.5 2 3.6 2.2 7H9.8C10 7.6 10.8 5.5 12 4zM4.1 13h3.7c.1 2.4.7 4.6 1.6 6.3A8 8 0 0 1 4.1 13zm0-2a8 8 0 0 1 5.3-6.3c-.9 1.7-1.5 3.9-1.6 6.3zm5.7 2h4.4c-.2 3.4-1 5.5-2.2 7-1.2-1.5-2-3.6-2.2-7zm6.4 0h3.7a8 8 0 0 1-5.3 6.3c.9-1.7 1.5-3.9 1.6-6.3zm0-2c-.1-2.4-.7-4.6-1.6-6.3A8 8 0 0 1 19.9 11z"/></svg>www.meridianhose.com.au</li>
      <li><svg viewBox="0 0 24 24"><path d="M12 2a7 7 0 0 0-7 7c0 5 7 13 7 13s7-8 7-13a7 7 0 0 0-7-7zm0 9.5A2.5 2.5 0 1 1 12 6.5a2.5 2.5 0 0 1 0 5z"/></svg>421, Address line here</li>
      <li class="no-icon">Country Name, 45452</li>
    </ul>

    <p class="slogan">Industry chosen hose and fittings provider</p>
  </section>

</body>
</html>
```